I need a new business card for my hair salon based in Fairfax, VA called "Lune's Salon". I have been in business at the same location for the past 15 years, and have recently remodeled the place to be a little bit more upscale and modern. Previously, my clientele's were mostly men, but now I would like to attract more female clientele into my business. I would like the design to attract the female's attention with it's modern touch, flowery, freshness with just enough information and not too compact. Simple, clean and professional is the look.
Requirements
Must Have:
- The design should include:
Business name: Lune's Salon
Hairstylist/Owner Name: Lune Okafor
Phone Number: (555) 418-6037
Website: www.lunehairstudio.example
Address: 48390 Harlow Penn Circle
Fairfax, VA 20517
FRONT CARD should include:
- Logo (Business name)
- Slogan (Soft curls, bright days)
BACK CARD should include:
- Logo (Business name)
- Hairstyle name
- Phone number
- Website
- Address
Reason: There were some good submission for this project, but most of the submission were poorly designed, and did not have what I want. There isn't enough designs for me to choose from and not one of it stood out to me. I would like to extend it a bit longer to see if any other designer would step up to the plate, and deliver. Thank you.
Requirements
Must have
- The front side of the business card should only have the business name (Lune's Salon) and slogan, (Soft curls bright days) with a creative design.
The back side of the business card should have all the business information, and creative design that matches with the front, but not identical.
The first letter (V) in (Lune's) should have a flower design connected to it, which blends into the background design.
Nice to have
- Light color scheme.
Should not have
- The front, and back should not have the same design.
Do not include illustrations of a pair of scissors, combs or any objects in the design.
The design should not take the main focus from the business name and business information. It should blend well together... if that's possible.

```html
<!DOCTYPE html>
<html lang="en">
<head>
<meta charset="utf-8">
<title>Lune's Salon – Business Cards</title>
<link href="https://fonts.googleapis.com/css2?family=Lato:wght@300;400;700&display=swap" rel="stylesheet">
<style>
  :root {
    --stage: #2d2d2d;
    --card-dark: #242424;
    --card-orange: #e5711b;
    --pink: #ff8585;
    --white: #ffffff;
    --ink: #2a2a2a;
    --flourish-dark: #3a3a3a;
    --flourish-orange: #f49a45;
  }
  * { margin: 0; padding: 0; box-sizing: border-box; }
  html, body {
    width: 1025px;
    height: 1200px;
    overflow: hidden;
    background: var(--stage);
    font-family: Arial, Helvetica, sans-serif;
  }
  .stage { position: relative; width: 1025px; height: 1200px; }

  .card {
    position: absolute;
    left: 145px;
    width: 740px;
    height: 396px;
    overflow: hidden;
  }
  .card--back { top: 133px; background: var(--card-dark); }
  .card--front { top: 648px; background: var(--card-orange); }

  .contact-bar {
    position: absolute;
    top: 26px;
    right: 24px;
    font-size: 14px;
    color: var(--white);
    white-space: nowrap;
  }
  .contact-bar .stylist-name,
  .contact-bar .phone { font-weight: 700; }
  .contact-bar .divider { margin: 0 8px; color: var(--white); }

  .brand-name {
    position: absolute;
    left: 136px;
    font-family: "Lato", Arial, sans-serif;
    font-weight: 300;
    font-size: 78px;
    line-height: 1;
    letter-spacing: 1px;
    white-space: nowrap;
  }
  .card--back .brand-name { top: 100px; color: var(--pink); }
  .card--front .brand-name { top: 112px; color: var(--white); }

  .slogan {
    position: absolute;
    left: 254px;
    font-family: "Lato", Arial, sans-serif;
    font-weight: 300;
    font-size: 33px;
    line-height: 1;
    white-space: nowrap;
  }
  .card--back .slogan { top: 212px; color: var(--white); }
  .card--back .slogan .accent { color: var(--pink); }
  .card--front .slogan { top: 226px; color: var(--ink); }
  .card--front .slogan .accent { color: var(--white); }

  .address {
    position: absolute;
    left: 254px;
    top: 274px;
    font-size: 13px;
    font-style: normal;
    line-height: 20px;
    color: var(--white);
  }
  .address .website { font-weight: 700; }

  .flourish-band {
    position: absolute;
    left: 0;
    bottom: 0;
    width: 100%;
    height: 76px;
  }
  .card--back .flourish-band {
    background: linear-gradient(to bottom, rgba(58,58,58,0) 0%, var(--flourish-dark) 75%);
  }
  .card--front .flourish-band {
    background: linear-gradient(to bottom, rgba(244,154,69,0) 0%, var(--flourish-orange) 75%);
  }
</style>
</head>
<body>
<main class="stage">

  <section class="card card--back" aria-label="Back of card">
    <p class="contact-bar"><span class="stylist-name">LUNE OKAFOR -</span> Hairstylist<span class="divider">|</span><span class="phone">Phone: (555) 418-6037</span></p>
    <h1 class="brand-name">Lune's Salon</h1>
    <p class="slogan">Soft <span class="accent">curls</span>, bright <span class="accent">days</span></p>
    <address class="address">
      <span>48390 Harlow Penn Circle, Fairfax, VA 20517</span><br>
      <span class="website">www.lunehairstudio.example</span>
    </address>
    <div class="flourish-band" role="img" aria-label="Flowery grey scroll ornament along the bottom edge"></div>
  </section>

  <section class="card card--front" aria-label="Front of card">
    <h2 class="brand-name">Lune's Salon</h2>
    <p class="slogan">Soft <span class="accent">curls</span>, bright <span class="accent">days</span></p>
    <div class="flourish-band" role="img" aria-label="Flowery light orange scroll ornament along the bottom edge"></div>
  </section>

</main>
</body>
</html>
```